Estate Agent/Real Estate valuation tool

We need a design for our our new estate agent valuation tool.

The tool allows users to book a valuation of their house/property with the estate agent, after they choose there property they can then complete their details and choose a booking time.

The mock up of the design we want is attached to this project.(Main Screen)

This also needs to be responsive so the design is easy to use on a mobile device.

Target Market(s)

estate agents

Industry/Entity Type

Real Estate Agent

Number of Pages Required

1 page

Requirements
Must have
• Section 2 and 3 greyed out when user is on step 1
• Section 1 and 3 greyed out when user is on step 2
• Section 1 and 2 greyed out when the user is on step 3
• *** Design must be shown for mobile/ipad and desktop
Nice to have
• Clean and Simple
Should not have
• Dark colours

```html
<!DOCTYPE html>
<html lang="en">
<head>
<meta charset="utf-8">
<title>Real Estate Valuation – Book Your Valuation Online</title>
<link rel="stylesheet" href="https://fonts.googleapis.com/css2?family=Noto+Serif:wght@400;700&family=Source+Sans+3:wght@300;400;600;700&display=swap">
<style>
  :root {
    --page-bg: #f2f2f2;
    --white: #ffffff;
    --ink: #1c1c1c;
    --ink-soft: #444444;
    --field-text: #5a5a5a;
    --green: #3aaa4b;
    --green-dark: #218a34;
    --panel-light: #e6e6e6;
    --panel-light-border: #cfcfcf;
    --panel-dark: #1e1e1e;
    --button-muted: #4a4a4a;
    --search-bg: #555555;
    --field-border: #d2d2d2;
    --chip-bg: #e2e2e2;
  }
  * { box-sizing: border-box; margin: 0; padding: 0; }
  html, body { width: 1200px; height: 674px; overflow: hidden; }
  body {
    position: relative;
    background: linear-gradient(var(--page-bg) 0 200px, var(--white) 200px);
    font-family: "Noto Serif", Georgia, serif;
    color: var(--ink);
  }

  /* Header */
  .brand-illustration {
    position: absolute; left: 553px; top: 33px; width: 94px; height: 57px;
    background: linear-gradient(#3a3a3a, #1c1c1c);
    clip-path: polygon(0 100%, 18% 35%, 30% 35%, 34% 15%, 48% 0, 60% 15%, 64% 30%, 82% 30%, 100% 100%);
  }
  .brand-name {
    position: absolute; left: 0; width: 1200px; top: 90px;
    text-align: center; font-size: 27px; font-weight: 700; color: var(--ink);
  }
  .page-title {
    position: absolute; left: 0; width: 1200px; top: 153px;
    text-align: center; font-family: "Source Sans 3", Arial, sans-serif;
    font-weight: 400; font-size: 25px; color: var(--ink-soft);
  }

  /* Step band */
  .steps {
    position: absolute; left: 0; top: 198px; width: 1200px; height: 60px;
    background: var(--green);
  }
  .steps::before, .steps::after {
    content: ""; position: absolute; left: 0; right: 0;
    border-top: 1px dashed var(--white);
  }
  .steps::before { top: 2px; }
  .steps::after { bottom: 2px; }
  .steps-arrow { position: absolute; left: 0; top: 0; }
  .step {
    position: absolute; top: 9px; display: flex; align-items: center; gap: 7px;
    font-family: "Source Sans 3", Arial, sans-serif; font-weight: 700;
    font-size: 16.5px; color: var(--white); letter-spacing: .1px;
  }
  .step-icon {
    width: 41px; height: 41px; border-radius: 50%;
    background: rgba(0,0,0,.18); display: flex; align-items: center; justify-content: center;
  }
  .step--property { left: 118px; }
  .step--details { left: 446px; }
  .step--time { left: 774px; }

  /* Panels */
  .panel {
    position: absolute; top: 276px; width: 309px; height: 350px; padding: 12px 9px 0;
  }
  .panel--property { left: 116px; background: var(--panel-light); border: 1px solid var(--panel-light-border); }
  .panel--details { left: 445px; background: var(--panel-dark); }
  .panel--time { left: 775px; background: var(--panel-dark); padding: 12px 6px 0; }

  .field {
    display: flex; height: 40px; margin-bottom: 7px;
    background: var(--white); border: 1px solid var(--field-border); border-radius: 2px;
    align-items: center; padding-left: 10px;
    font-size: 13px; color: var(--field-text);
  }
  .field--search { padding-right: 0; }
  .field--search span { flex: 1; }
  .search-button {
    width: 39px; height: 40px; margin: -1px -1px -1px 0;
    background: var(--search-bg); display: flex; align-items: center; justify-content: center;
    border-radius: 0 2px 2px 0;
  }

  .action {
    position: absolute; left: 10px; right: 10px; bottom: 10px; height: 39px;
    display: flex; align-items: center; justify-content: center;
    font-weight: 700; font-size: 15.5px; color: var(--white);
    text-shadow: 0 1px 1px rgba(0,0,0,.35); letter-spacing: .2px;
    background: var(--button-muted);
  }
  .panel--property .action { background: var(--green-dark); }
  .panel--time .action { left: 8px; right: 7px; }

  .day-tabs { display: flex; gap: 2.8px; margin-bottom: 8px; }
  .day-tab {
    width: 40.5px; height: 39px; background: var(--white); border-radius: 2px;
    display: flex; align-items: center; justify-content: center;
    font-size: 7.5px; font-weight: 700; color: var(--ink); white-space: nowrap; letter-spacing: -.2px;
  }
  .day-tab--active { background: var(--green); color: var(--white); font-weight: 400; }

  .slot {
    display: flex; align-items: center; justify-content: space-between;
    height: 40px; margin-bottom: 7.7px; padding: 0 6px 0 9px;
    background: var(--white); border-radius: 2px;
    font-size: 13px; color: var(--field-text);
  }
  .slot-time {
    width: 57px; height: 27px; background: var(--chip-bg); border-radius: 3px;
    display: flex; align-items: center; justify-content: center;
    font-weight: 700; font-size: 13.5px; color: var(--ink);
  }
</style>
</head>
<body>
  <header>
    <div class="brand-illustration" role="img" aria-label="Line drawing of city buildings"></div>
    <h1 class="brand-name">Real Estate Valuation</h1>
    <h2 class="page-title">BOOK YOUR VALUATION ONLINE</h2>
  </header>

  <nav class="steps" aria-label="Booking steps">
    <svg class="steps-arrow" width="1200" height="60" viewBox="0 0 1200 60" aria-hidden="true">
      <polygon points="347,3 683,3 711,30 683,57 347,57 374,30" fill="#218a34"/>
    </svg>
    <div class="step step--property">
      <span class="step-icon">
        <svg width="28" height="26" viewBox="0 0 28 26" aria-hidden="true">
          <path d="M2 13 L14 2 L26 13" fill="none" stroke="#fff" stroke-width="2.6" stroke-linejoin="round"/>
          <path d="M6 12 V24 H22 V12" fill="none" stroke="#fff" stroke-width="2.4"/>
          <circle cx="14" cy="12" r="1.6" fill="#fff"/>
          <rect x="12.6" y="15" width="2.8" height="7" fill="#fff"/>
        </svg>
      </span>
      PROPERTY DETAILS
    </div>
    <div class="step step--details">
      <span class="step-icon">
        <svg width="30" height="30" viewBox="0 0 30 30" aria-hidden="true">
          <circle cx="15" cy="15" r="14" fill="#fff"/>
          <circle cx="16" cy="8.5" r="2.3" fill="#218a34"/>
          <path d="M12 13 H17 L15 22 H18 L17.6 24 H11.5 L13.4 15 H11.6 Z" fill="#218a34"/>
        </svg>
      </span>
      YOUR DETAILS
    </div>
    <div class="step step--time">
      <span class="step-icon">
        <svg width="30" height="30" viewBox="0 0 30 30" aria-hidden="true">
          <path d="M15 2 A13 13 0 1 0 28 15" fill="none" stroke="#fff" stroke-width="2"/>
          <path d="M28 15 A13 13 0 0 0 15 2" fill="none" stroke="#fff" stroke-width="2" stroke-dasharray="2 2.5"/>
          <path d="M15 7 V15 L21 18" fill="none" stroke="#fff" stroke-width="2.2" stroke-linecap="round"/>
        </svg>
      </span>
      APPOINTMENT TIME
    </div>
  </nav>

  <main>
    <section class="panel panel--property" aria-label="Property details">
      <div class="field field--search">
        <span>125648</span>
        <span class="search-button">
          <svg width="22" height="22" viewBox="0 0 22 22" aria-hidden="true">
            <circle cx="9" cy="9" r="7" fill="none" stroke="#fff" stroke-width="1.6"/>
            <line x1="14" y1="14" x2="20.5" y2="20.5" stroke="#fff" stroke-width="1.8" stroke-linecap="round"/>
          </svg>
        </span>
      </div>
      <div class="field">123 Test Street</div>
      <div class="field">Test City</div>
      <div class="field">Test Country</div>
      <div class="action">PROCEED</div>
    </section>

    <section class="panel panel--details" aria-label="Your details">
      <div class="field">Your Name:</div>
      <div class="field">Your Email:</div>
      <div class="field">Yout Contact No.</div>
      <div class="action">PROCEED</div>
    </section>

    <section class="panel panel--time" aria-label="Appointment time">
      <div class="day-tabs">
        <div class="day-tab">Today</div>
        <div class="day-tab day-tab--active">Tomorrow</div>
        <div class="day-tab">Mon - 30th</div>
        <div class="day-tab">Tue - 1st</div>
        <div class="day-tab">Wed - 2nd</div>
        <div class="day-tab">Thus - 4th</div>
        <div class="day-tab">Fri - 5th</div>
      </div>
      <div class="slot">Sunday 29th November <span class="slot-time">08:30</span></div>
      <div class="slot">Sunday 29th November <span class="slot-time">10:30</span></div>
      <div class="slot">Sunday 29th November <span class="slot-time">12:30</span></div>
      <div class="slot">Sunday 29th November <span class="slot-time">14:30</span></div>
      <div class="slot">Sunday 29th November <span class="slot-time">16:30</span></div>
      <div class="action">CONFIRM BOOKING</div>
    </section>
  </main>
</body>
</html>
```